Cole Varga Photography

Would like the Business card to have a cool logo. I’m targeting wedding/ engagement: portrait photography. My phone number on it. And my business email address.

Wedding/portrait/engagement photography.

```html
<!DOCTYPE html>
<html lang="en">
<head>
<meta charset="utf-8">
<title>Cole Varga Photography – Business Card</title>
<link href="https://fonts.googleapis.com/css2?family=Jost:wght@400;500&display=swap" rel="stylesheet">
<style>
  :root {
    --backdrop: #c4c6c5;
    --card-ink: #141414;
    --card-ink-soft: #2a2a2a;
    --name-white: #f4f4f4;
    --contact-grey: #b9b9b9;
    --divider: #3a3a3a;
    --mark-grey: #8a8a8a;
  }
  * { margin: 0; padding: 0; box-sizing: border-box; }
  html, body {
    width: 1200px;
    height: 694px;
    overflow: hidden;
    background: var(--backdrop);
  }
  .canvas {
    position: relative;
    width: 1200px;
    height: 694px;
    display: flex;
    align-items: center;
    justify-content: center;
  }
  .business-card {
    position: relative;
    width: 880px;
    height: 503px;
    background: radial-gradient(ellipse at 40% 35%, var(--card-ink-soft) 0%, var(--card-ink) 75%);
    box-shadow: 0 18px 40px rgba(0,0,0,0.28);
    overflow: hidden;
  }
  .card-texture {
    position: absolute;
    inset: 0;
    background: linear-gradient(160deg, rgba(255,255,255,0.04), rgba(0,0,0,0.15));
  }
  .wordmark {
    position: absolute;
    left: 0;
    right: 0;
    top: 150px;
    display: flex;
    justify-content: center;
  }
  .wordmark-name {
    display: inline-flex;
    align-items: center;
    gap: 16px;
    font-family: "Jost", sans-serif;
    font-weight: 500;
    font-size: 44px;
    color: var(--name-white);
    letter-spacing: 1px;
  }
  .wordmark-dot {
    width: 14px;
    height: 14px;
    border-radius: 50%;
    background: var(--mark-grey);
  }
  .client-name {
    position: absolute;
    left: 125px;
    top: 345px;
    font-family: "Jost", sans-serif;
    font-weight: 500;
    font-size: 34px;
    color: var(--name-white);
    letter-spacing: 1px;
  }
  .contact-block {
    position: absolute;
    left: 500px;
    top: 325px;
    padding-left: 22px;
    border-left: 1px solid var(--divider);
    font-family: "Jost", sans-serif;
    font-weight: 400;
    font-size: 22px;
    color: var(--contact-grey);
    letter-spacing: 1px;
  }
  .contact-line {
    display: flex;
    align-items: center;
    gap: 16px;
    height: 44px;
  }
  .contact-icon { width: 18px; height: 18px; fill: var(--contact-grey); }
  .contact-icon--mail { fill: none; stroke: var(--contact-grey); stroke-width: 1.8; }
</style>
</head>
<body>
<main class="canvas">
  <article class="business-card">
    <div class="card-texture" role="img" aria-label="Dark black textured paper surface"></div>

    <header class="wordmark">
      <div class="wordmark-name"><span class="wordmark-dot"></span>Cole Varga Photography</div>
    </header>

    <p class="client-name">CLIENT NAME</p>

    <section class="contact-block">
      <div class="contact-line">
        <svg class="contact-icon" viewBox="0 0 24 24" aria-hidden="true">
          <path d="M6.6 10.8a15.1 15.1 0 0 0 6.6 6.6l2.2-2.2a1 1 0 0 1 1-.25 11.4 11.4 0 0 0 3.6.57 1 1 0 0 1 1 1V20a1 1 0 0 1-1 1A17 17 0 0 1 3 4a1 1 0 0 1 1-1h3.5a1 1 0 0 1 1 1c0 1.25.2 2.45.57 3.57a1 1 0 0 1-.25 1z"/>
        </svg>
        <span>555.014.2290</span>
      </div>
      <div class="contact-line">
        <svg class="contact-icon contact-icon--mail" viewBox="0 0 24 24" aria-hidden="true">
          <path d="M2 5h20v14H2z M3.5 6.5 12 13l8.5-6.5"/>
        </svg>
        <span>hello@colevargaphoto.com</span>
      </div>
    </section>
  </article>
</main>
</body>
</html>
```